Corvale Mechanical - Letterhead

We are a plumbing and hvac company based in Calgary. This letterhead will be on our quotes, invoices, preventative maintenance proposals etc.

```html
<!DOCTYPE html>
<html lang="en">
<head>
<meta charset="utf-8">
<title>Corvale Mechanical – Letterhead</title>
<link href="https://fonts.googleapis.com/css2?family=Russo+One&display=swap" rel="stylesheet">
<style>
  :root {
    --backdrop: #d6d6d6;
    --paper: #ffffff;
    --brand-orange: #ef6337;
    --brand-blue: #3a78c2;
    --watermark-peach: #fce6df;
    --watermark-blue: #e2eaf5;
  }
  html, body {
    margin: 0;
    padding: 0;
    width: 1200px;
    height: 1200px;
    overflow: hidden;
    background: var(--backdrop);
  }
  .letterhead {
    position: absolute;
    left: 290px;
    top: 170px;
    width: 580px;
    height: 820px;
    background: var(--paper);
  }
  .letterhead-art {
    display: block;
    width: 100%;
    height: 100%;
  }
  .header-band { fill: var(--brand-orange); }
  .header-rule { fill: none; stroke: var(--brand-blue); stroke-width: 9; }
  .brand-dot { fill: var(--brand-orange); }
  .brand-name {
    font-family: "Russo One", sans-serif;
    fill: var(--brand-blue);
  }
  .brand-name-main { font-size: 44px; letter-spacing: 2px; }
  .brand-name-sub { font-size: 19px; letter-spacing: 3px; }
</style>
</head>
<body>
  <section class="letterhead" aria-label="Corvale Mechanical letterhead">
    <svg class="letterhead-art" viewBox="0 0 966 1366">
      <defs>
        <radialGradient id="watermarkGlow" cx="50%" cy="50%" r="50%">
          <stop offset="0%" stop-color="var(--watermark-blue)"/>
          <stop offset="45%" stop-color="var(--watermark-peach)"/>
          <stop offset="100%" stop-color="var(--watermark-peach)"/>
        </radialGradient>
      </defs>

      <path class="header-band" d="M0 0 H966 V212 Q483 -6 0 212 Z"/>
      <path class="header-rule" d="M0 228 Q483 8 966 228"/>

      <circle class="brand-dot" cx="483" cy="188" r="44"/>
      <text class="brand-name brand-name-main" x="483" y="278" text-anchor="middle">CORVALE</text>
      <text class="brand-name brand-name-sub" x="483" y="304" text-anchor="middle">MECHANICAL INC</text>

      <g role="img" aria-label="Faint brand watermark in soft peach and light blue">
        <circle cx="483" cy="838" r="330" fill="url(#watermarkGlow)"/>
      </g>
    </svg>
  </section>
</body>
</html>
```